KRV Ferrowind, LLC. - Georgetown, KY - Chicago, IL

Create a company brochure for KRV Ferrowind.
Does process off spec UBC cost you?
-Slower throughput, Double Runs
-Extra Manpower, more picking stations
-Redundant Final Quality Inspections
-Aluminum in the Residue
KRV Ferrowind with our Torvalen Designed and Bulit Custom UBC Specific processing center.
-Guaranteed No Rejections
-Increased cash flow with no rejection delays
-Reduce Manpower Costs
-Increase Total TPH thru your plant
More aluminum recovered - less in your residue
We can eliminate any quality concerns you have with UBC. This will allow you to streamline your operation and concentrate on moving all of your material faster and more efficiently.
We can purchase your baled UBC directly with fast payment or toll process them guaranteeing mill spec.
B2B, Waste Recycling Companies, Aluminum Can Recyclers, Aluminum can Brokers, Aluminum Can Mills
Recycling
- You do not have to use the attached photo. It is just an example.

```html
<!DOCTYPE html>
<html lang="en">
<head>
<meta charset="utf-8">
<title>KRV Ferrowind Brochure Cover</title>
<link rel="stylesheet" href="https://fonts.googleapis.com/css2?family=Bitter:wght@700&display=swap">
<style>
  :root {
    --backdrop: #ece6dc;
    --cover: #1d1b1c;
    --gold: #d4a21a;
    --gold-light: #f2d34a;
    --gold-dark: #9a6d0a;
    --copper-light: #e8a27c;
    --copper: #c46a43;
    --copper-dark: #6e3a22;
    --band: #0f2533;
    --band-edge: #7f98a6;
    --tagline: #d3dde2;
  }
  html, body {
    margin: 0;
    width: 1200px;
    height: 1200px;
    overflow: hidden;
    background: var(--backdrop);
  }
  .brochure-cover {
    position: absolute;
    left: 160px;
    top: 30px;
    width: 881px;
    height: 1140px;
    background: var(--cover);
  }
  .brand-name {
    position: absolute;
    top: 247px;
    left: 0;
    width: 100%;
    text-align: center;
    margin: 0;
    font-family: "Bitter", serif;
    font-weight: 700;
    font-size: 66px;
    line-height: 80px;
    color: var(--gold);
  }
  .gold-rule {
    position: absolute;
    left: 0;
    width: 100%;
    height: 13px;
    background: linear-gradient(90deg, var(--gold-dark), var(--gold) 25%, var(--gold-light) 50%, var(--gold) 75%, var(--gold-dark));
  }
  .gold-rule--top { top: 415px; }
  .gold-rule--bottom { top: 711px; }
  .hero-photo {
    position: absolute;
    top: 428px;
    left: 0;
    width: 100%;
    height: 283px;
    background:
      radial-gradient(ellipse at 35% 55%, var(--copper-light), transparent 60%),
      linear-gradient(120deg, var(--copper-dark), var(--copper) 40%, var(--copper-light) 60%, var(--copper) 80%, var(--copper-dark));
  }
  .tagline-band {
    position: absolute;
    top: 780px;
    left: 0;
    width: 100%;
    height: 85px;
    box-sizing: border-box;
    background: var(--band);
    border-top: 3px solid var(--band-edge);
    border-bottom: 3px solid var(--band-edge);
    display: flex;
    align-items: center;
    justify-content: center;
  }
  .tagline {
    margin: 0;
    font-family: "Bitter", serif;
    font-weight: 700;
    font-size: 39px;
    color: var(--tagline);
    white-space: nowrap;
  }
</style>
</head>
<body>
  <main class="brochure-cover">
    <h1 class="brand-name">KRV Ferrowind</h1>
    <div class="gold-rule gold-rule--top"></div>
    <div class="hero-photo" role="img" aria-label="Close-up photograph of tangled shiny copper wire scrap"></div>
    <div class="gold-rule gold-rule--bottom"></div>
    <div class="tagline-band">
      <p class="tagline">Recycling Solutions Built on Integrity</p>
    </div>
  </main>
</body>
</html>
```